Homes, Invest in Non-performing loans

We need only 3 web pages, one for the home, one for the content, one for the properties.
The main focus of our business is to offer non performing loans (before foreclosures) to the general public. All the non-performing mortgages will end in a house, an apartment, a store, etc.
Our customers are able to invest from 10,000usd to 1,000,000usd (average 50,000usd).
Our customers' usual focus groups are employees who want second earnings, perceiving the business feeling without outlay time. They look for a solid finance sense corporation that confers them certainty.
Nearly all our clients desire the house, apartment, store, etc. more than the actual earnings.
The name of our company is BRAMLEY
Reason: We value the time and effort you already invest in our project. We realize that we did't come back on some of the doubts requested by the designers. It will be inequitable to the designers who prerequisite our feedback. We also appreciate the comprehension of the community in this postponement.
Reason: Designers,
We really apreciate all the time and effort you put on our project. From the begining we ask for 3 pages, so now we will leave the 10 finalist and provide some extra time to submit the other 2 pages.
We will race the price in 10%
Target Market(s)
Our customers average investors works as employees and want to have a second income or business without spending time. (People from 35 to 50)
Industry/Entity Type
Finance
Requirements
Should not have
- FLASH

```html
<!DOCTYPE html>
<html lang="es">
<head>
<meta charset="utf-8">
<title>BRAMLEY · Remates Hipotecarios</title>
<link rel="stylesheet" href="https://fonts.googleapis.com/css2?family=Questrial&family=Montserrat:wght@700&display=swap">
<style>
:root{
  --slate:#6e7378;
  --slate-dark:#5d6166;
  --olive:#9a9a2c;
  --ink:#1e1d1e;
  --night:#232223;
  --orange:#f39a1d;
  --red:#c8141e;
  --paper:#ffffff;
  --text:#4a4a4a;
  --footer:#a4a9ae;
}
*{margin:0;padding:0;box-sizing:border-box}
html,body{width:1200px;height:1124px;overflow:hidden;background:var(--paper)}
body{position:relative;font-family:"Questrial",sans-serif;color:var(--text)}
.abs{position:absolute}

/* header bands */
.top-band{left:0;top:0;width:1200px;height:98px;background:linear-gradient(#7a7e83,var(--slate-dark))}
.olive-rule{left:0;height:5px;width:1200px;background:var(--olive)}
.dark-band{left:0;top:101px;width:1200px;height:356px;background:var(--night)}

.utility{right:48px;top:22px;display:flex;align-items:center;gap:10px;color:#fff;font-size:10px;letter-spacing:.3px}
.utility .call{font-size:14px;font-weight:bold;display:flex;align-items:center;gap:5px}
.utility .call svg{width:16px;height:16px}

/* logo panel */
.brand-panel{left:0;top:133px;width:332px;height:267px;background:var(--paper);box-shadow:10px 0 0 #3a393a}
.brand-name{left:58px;top:105px;display:flex;align-items:center;gap:10px;font-size:40px;color:#2f2f30;letter-spacing:1px}
.brand-name .mark{width:30px;height:30px;background:var(--olive)}
.brand-tag{left:58px;top:232px;font-size:14px;letter-spacing:2.6px;color:#333}

/* hero */
.hero{left:310px;top:52px;width:847px;height:450px;background:linear-gradient(110deg,#e9eef0 0%,#d7d9d6 30%,#a8b3c0 55%,#dfe2e4 80%,#c9c5c1 100%)}
.hero-title{left:380px;top:418px;color:var(--orange);font-family:"Montserrat",sans-serif;font-weight:700;line-height:1}
.hero-title .small{font-size:22px;letter-spacing:.5px}
.hero-title .big{font-size:48px;letter-spacing:-1px}

.main-nav{left:635px;top:43px;width:522px;height:30px;background:var(--olive);border-radius:14px 0 0 0;display:flex;align-items:center;padding-left:20px}
.main-nav a{color:#fff;text-decoration:none;font-size:14px;padding:0 12px;border-left:2px solid #fff;line-height:16px}
.main-nav a:first-child{border-left:none;padding-left:0}
.search{margin-left:auto;margin-right:10px;display:flex;align-items:center;gap:4px}
.search span{display:block;width:114px;height:14px;background:#fff}
.search svg{width:15px;height:15px}

.social{left:1162px;top:134px;display:flex;flex-direction:column;gap:5px}
.social span{width:17px;height:16px;background:#e8e8e8}
.slider-dots{left:1165px;top:410px;display:flex;flex-direction:column;gap:4px}
.slider-dots span{width:11px;height:11px;border-radius:50%;background:#9a9a9a}
.slider-dots span:last-child{background:#e6e6e6}

/* intro */
.intro{left:312px;top:558px;width:398px;font-size:12px;line-height:18.2px;text-align:justify}

/* featured */
.photo{background:linear-gradient(180deg,#9fb8d6 0%,#c9d7e6 35%,#d49a76 60%,#b9825f 82%,#6f7a68 100%)}
.price{background:var(--red);color:#fff;display:flex;align-items:center;justify-content:center;gap:16px;font-size:17px}
.price s{text-decoration:line-through}
.feature-photo{left:739px;top:551px;width:169px;height:104px;border:2px solid #fff;box-shadow:0 0 3px rgba(0,0,0,.3)}
.feature-price{left:739px;top:655px;width:169px;height:26px}
.feature-card{left:908px;top:561px;width:242px;height:94px;background:var(--orange);color:#fff;padding:12px 10px 0 17px;overflow:hidden}
.feature-card h3{font-weight:normal;font-size:13px;white-space:nowrap;margin-bottom:9px;letter-spacing:.2px}
.feature-card p{font-size:7.8px;line-height:11px}

/* listing grid */
.listing{position:absolute;top:715px;width:169px}
.listing .photo{height:104px}
.listing .price{height:26px}
.listing p{margin-top:10px;font-size:11px;line-height:14px;text-align:left}

/* footer */
.footer{left:0;top:927px;width:1200px;height:149px;background:var(--footer)}
.footer::before{content:"";position:absolute;left:0;top:0;width:100%;height:7px;
  background:linear-gradient(135deg,#fff 50%,transparent 50%) 0 0/10px 10px repeat-x,
             linear-gradient(225deg,#fff 50%,transparent 50%) 0 0/10px 10px repeat-x}
.footer-nav{left:309px;top:40px;display:flex;color:#fff;font-size:14px}
.footer-nav a{color:#fff;text-decoration:none}
.footer-nav .sep{width:1px;height:20px;background:#fff;margin-top:-2px}
.pay-note{left:810px;top:70px;font-size:6.5px;color:#fff}
.pay-badges{left:733px;top:79px;display:flex;gap:5px}
.pay-badges span{width:37px;height:21px;background:#f4f4f4;border-radius:2px}
.footer-divider{left:951px;top:18px;width:1px;height:82px;background:#fff}
.contact{left:979px;color:#fff;display:flex;align-items:center}
.contact svg{width:22px;height:22px}
.contact-call{top:25px;font-size:10px;gap:6px}
.contact-call b{font-size:14px;letter-spacing:.5px;margin-right:24px}
.contact-chat{top:53px;font-size:10px;gap:20px}

.base-band{left:0;top:1076px;width:1200px;height:48px;background:var(--ink)}
.copyright{right:66px;top:17px;color:#fff;font-size:10.5px}
</style>
</head>
<body>

<header>
  <div class="abs top-band"></div>
  <div class="abs olive-rule" style="top:96px"></div>
  <div class="abs dark-band"></div>
  <div class="abs olive-rule" style="top:457px"></div>

  <div class="abs utility">
    <span class="call">
      <svg viewBox="0 0 24 24"><path fill="#fff" d="M6.6 10.8a15 15 0 0 0 6.6 6.6l2.2-2.2c.3-.3.7-.4 1-.2 1.1.4 2.3.6 3.6.6.6 0 1 .4 1 1V20c0 .6-.4 1-1 1A17 17 0 0 1 3 4c0-.6.4-1 1-1h3.5c.6 0 1 .4 1 1 0 1.3.2 2.5.6 3.6.1.3 0 .7-.2 1z"/></svg>
      Call: 000 00 000
    </span>
    <span>LOGIN | CREATE AN ACCOUNT</span>
  </div>

  <div class="abs brand-panel">
    <div class="abs brand-name"><span class="mark"></span>BRAMLEY</div>
    <div class="abs brand-tag">REMATES HIPOTECARIOS</div>
  </div>

  <div class="abs hero" role="img" aria-label="Photo of a smiling couple receiving house keys from an agent in a bright home"></div>
  <div class="abs hero-title">
    <div class="small">NON-PERFORMING</div>
    <div class="big">MORTGAGES</div>
  </div>

  <nav class="abs main-nav">
    <a href="#">HOME</a><a href="#">PROPERTIES</a><a href="#">CONTENT</a>
    <div class="search"><span></span>
      <svg viewBox="0 0 16 16"><circle cx="9.5" cy="6.5" r="4.5" fill="none" stroke="#fff" stroke-width="2"/><line x1="6.3" y1="9.7" x2="1.5" y2="14.5" stroke="#fff" stroke-width="2.4"/></svg>
    </div>
  </nav>

  <div class="abs social"><span></span><span></span><span></span></div>
  <div class="abs slider-dots"><span></span><span></span><span></span></div>
</header>

<main>
  <p class="abs intro">BRAMLEY® Remates Hipotecarios, somos una empresa, un holding y una marca, con experiencia comprobable dedicada a la compra, venta y ejecución de Remates Hipotecarios en México que, de manera ética y legal, ofrecemos a nuestros inversionistas la satisfacción de adquirir atractivas oportunidades de vivienda con importantes ahorros; esto se traduce en ganancias. Los Remates Hipotecarios son la mejor forma de invertir a través de la adquisición de una propiedad con un costo inferior al 60% de su valor comercial.</p>

  <div class="abs feature-photo photo" role="img" aria-label="Photo of a brick apartment building"></div>
  <div class="abs feature-price price"><s>$ 0,000</s><span>$ 0,000</span></div>
  <article class="abs feature-card">
    <h3>Tláhuac . REMATE HIPOTECARIO</h3>
    <p>¡Atención inversionistas, gran oportunidad en Tláhuac! departamento 2 recámaras, 1 baño, estacionamiento, comedor, cocina, cerca de periférico, excelentes vías de comunicación.</p>
  </article>

  <article class="listing" style="left:312px">
    <div class="photo" role="img" aria-label="Photo of a brick apartment building"></div>
    <div class="price"><s>$ 0,000</s><span>$ 0,000</span></div>
    <p>BRAMLEY® Remates Hipotecarios, somos una empresa, un holding y una marca.</p>
  </article>
  <article class="listing" style="left:534px">
    <div class="photo" role="img" aria-label="Photo of a brick apartment building"></div>
    <div class="price"><s>$ 0,000</s><span>$ 0,000</span></div>
    <p>BRAMLEY® Remates Hipotecarios, somos una empresa, un holding y una marca.</p>
  </article>
  <article class="listing" style="left:756px">
    <div class="photo" role="img" aria-label="Photo of a brick apartment building"></div>
    <div class="price"><s>$ 0,000</s><span>$ 0,000</span></div>
    <p>BRAMLEY® Remates Hipotecarios, somos una empresa, un holding y una marca.</p>
  </article>
  <article class="listing" style="left:978px">
    <div class="photo" role="img" aria-label="Photo of a brick apartment building"></div>
    <div class="price"><s>$ 0,000</s><span>$ 0,000</span></div>
    <p>BRAMLEY® Remates Hipotecarios, somos una empresa, un holding y una marca.</p>
  </article>
</main>

<footer>
  <div class="abs footer">
    <nav class="abs footer-nav">
      <a href="#">HOME</a>
      <span class="sep" style="margin-left:58px;margin-right:50px"></span>
      <a href="#">PROPERTIES</a>
      <span class="sep" style="margin-left:54px;margin-right:52px"></span>
      <a href="#">CONTENT</a>
    </nav>
    <div class="abs pay-note">Pay your deposit now online</div>
    <div class="abs pay-badges"><span></span><span></span><span></span><span></span><span></span></div>
    <div class="abs footer-divider"></div>
    <div class="abs contact contact-call">Call: <b>XXX XXX XXX</b>
      <svg viewBox="0 0 24 24"><path fill="#fff" d="M6.6 10.8a15 15 0 0 0 6.6 6.6l2.2-2.2c.3-.3.7-.4 1-.2 1.1.4 2.3.6 3.6.6.6 0 1 .4 1 1V20c0 .6-.4 1-1 1A17 17 0 0 1 3 4c0-.6.4-1 1-1h3.5c.6 0 1 .4 1 1 0 1.3.2 2.5.6 3.6.1.3 0 .7-.2 1z"/></svg>
    </div>
    <div class="abs contact contact-chat">Click Here For Live Chat
      <svg viewBox="0 0 24 24"><path d="M4 14v-2a8 8 0 0 1 16 0v2" fill="none" stroke="#fff" stroke-width="2"/><rect x="3" y="13" width="4" height="7" rx="1.5" fill="#fff"/><rect x="17" y="13" width="4" height="7" rx="1.5" fill="#fff"/></svg>
    </div>
  </div>
  <div class="abs base-band"><div class="abs copyright">Copyright © 2012 All Rights Reserved.</div></div>
</footer>

</body>
</html>
```